Business Card Design

I would like a new business card design for an accounting firm that specializes in resolving clients tax problems. I want the card to give the impression that we are not your typical stodgy accounting firm, but at the same time we will get the job done.
Industry/Entity Type
Business
Contact Information for Business Card
Dorian T Welsby
Certified Public Accountant
38-27 52nd Street
Sunnyside, NY 11287
Tel: (718) 555-0142
Fax: (888) 555-0199
e-mail: dtwthecpa@ledgerpost.com
website: harborfilingreliefexperts.com

```html
<!DOCTYPE html>
<html lang="en">
<head>
<meta charset="utf-8">
<title>Dorian T Welsby – Business Card</title>
<link rel="stylesheet" href="https://fonts.googleapis.com/css2?family=Domine:wght@700&family=Open+Sans:wght@400&family=Oswald:wght@500&display=swap">
<style>
  :root {
    --backdrop: #3b3531;
    --card: #0d0d0e;
    --card-edge: #1b1b1d;
    --plate-blue: #1d4a8c;
    --plate-rim: #d9dde2;
    --accent-gold: #f0b21c;
    --text-light: #f2f2f2;
    --silver-hi: #f4f5f6;
    --silver-lo: #9ea2a7;
    --ink-dark: #2a2c30;
  }
  * { margin: 0; padding: 0; box-sizing: border-box; }
  html, body { width: 1200px; height: 900px; overflow: hidden; }
  body {
    background: var(--backdrop);
    position: relative;
    font-family: "Open Sans", sans-serif;
  }
  .card {
    position: absolute;
    top: 300px;
    width: 520px;
    height: 300px;
    background: var(--card);
    border: 1px solid var(--card-edge);
    box-shadow: 0 14px 30px rgba(0,0,0,0.45);
    overflow: hidden;
  }
  .card--front { left: 50px; }
  .card--back { left: 630px; }

  .name-plate {
    position: absolute;
    border-radius: 14px;
    text-align: center;
  }
  .card--front .name-plate {
    left: 28px; top: 52px;
    width: 264px; height: 68px;
    background: var(--plate-blue);
    border: 3px solid var(--plate-rim);
    padding-top: 9px;
  }
  .card--back .name-plate {
    left: 110px; top: 112px;
    width: 300px; height: 76px;
    background: linear-gradient(160deg, var(--silver-hi), var(--silver-lo) 60%, var(--silver-hi));
    padding-top: 11px;
  }
  .name-plate__name {
    font-family: "Domine", serif;
    font-weight: 700;
    letter-spacing: 2px;
    text-transform: uppercase;
    line-height: 1.15;
  }
  .card--front .name-plate__name { font-size: 21px; }
  .card--back .name-plate__name { font-size: 23px; }
  .name-plate__title {
    font-family: "Oswald", sans-serif;
    font-weight: 500;
    letter-spacing: 2.2px;
    text-transform: uppercase;
    margin-top: 2px;
  }
  .card--front .name-plate__title { font-size: 12px; }
  .card--back .name-plate__title { font-size: 13px; }
  .card--front .name-plate__name { color: var(--text-light); }
  .card--front .name-plate__title { color: var(--accent-gold); }
  .card--back .name-plate__name,
  .card--back .name-plate__title { color: var(--ink-dark); }

  .contact {
    position: absolute;
    left: 312px; top: 96px;
    width: 196px;
    color: var(--text-light);
    font-size: 12px;
    line-height: 1.45;
  }
  .contact__address { margin-bottom: 14px; }
  .contact__list { list-style: none; }
  .contact__item { display: flex; align-items: center; gap: 7px; white-space: nowrap; }
  .contact__icon { width: 10px; height: 10px; flex: none; fill: var(--accent-gold); }
</style>
</head>
<body>
  <section class="card card--front" aria-label="Card front">
    <div class="name-plate">
      <div class="name-plate__name">Dorian T Welsby</div>
      <div class="name-plate__title">Certified Public Accountant</div>
    </div>
    <div class="contact">
      <p class="contact__address">38-27 52nd Street<br>Sunnyside, NY 11287</p>
      <ul class="contact__list">
        <li class="contact__item">
          <svg class="contact__icon" viewBox="0 0 10 10"><path d="M2 0.5 L3.6 2.6 L2.7 3.6 Q3.8 5.9 6.3 7.2 L7.3 6.3 L9.5 7.9 L8.4 9.5 Q3.6 9 0.5 1.7 Z"/></svg>
          <span>(718) 555-0142</span>
        </li>
        <li class="contact__item">
          <svg class="contact__icon" viewBox="0 0 10 10"><rect x="2.5" y="0.5" width="5" height="3"/><rect x="0.5" y="3.5" width="9" height="5.5" rx="1"/></svg>
          <span>(888) 555-0199</span>
        </li>
        <li class="contact__item">
          <svg class="contact__icon" viewBox="0 0 10 10"><rect x="0.5" y="2" width="9" height="6.5"/><path d="M0.5 2 L5 6 L9.5 2" stroke="#0d0d0e" stroke-width="1" fill="none"/></svg>
          <span>dtwthecpa@ledgerpost.com</span>
        </li>
        <li class="contact__item">
          <svg class="contact__icon" viewBox="0 0 10 10"><path d="M4 6 L6 4" stroke="#f0b21c" stroke-width="1.2"/><path d="M5 2.5 L6.5 1 Q8 0 9 1 Q10 2 9 3.5 L7.5 5 M2.5 5 L1 6.5 Q0 8 1 9 Q2 10 3.5 9 L5 7.5" stroke="#f0b21c" stroke-width="1.2" fill="none"/></svg>
          <span>harborfilingreliefexperts.com</span>
        </li>
      </ul>
    </div>
  </section>

  <section class="card card--back" aria-label="Card back">
    <div class="name-plate">
      <div class="name-plate__name">Dorian T Welsby</div>
      <div class="name-plate__title">Certified Public Accountant</div>
    </div>
  </section>
</body>
</html>
```